Redesign of Brochure of company services

We need a redesign a brochure. All of the content on the existing brochure correct, but the design we are not pleased with it. I will provide the previous brochure. Every Window Bright is Angolan company that provides multiple service ranging providing fruits, vegetables, fisheries, and meat to multiple industries in angola. Every Window Bright seeks to start delivering or providing their service to home owners looking for fresh products. We want a brochure design that covers all of these aspects.

Target Market(s)

Home owners, middle and upper age mothers, middle and upper class

Industry/Entity Type

Retail

Requirements
Must have
• Logo of the company and the content info
Nice to have
• It's up to you

```html
<!DOCTYPE html>
<html lang="pt">
<head>
<meta charset="utf-8">
<title>Every Window Bright — Brochura</title>
<link href="https://fonts.googleapis.com/css2?family=Archivo+Black&family=Arimo:wght@400;700&display=swap" rel="stylesheet">
<style>
  :root{
    --stage:#3b3b3b;
    --paper:#ffffff;
    --paper-soft:#f1f1f1;
    --green:#3ea648;
    --green-dark:#2e8a37;
    --green-field:#5ea236;
    --green-field-deep:#3f7f25;
    --orange:#f08a24;
    --red:#e8372a;
    --blue:#1b8fd0;
    --ink:#1e1e1e;
    --white:#ffffff;
  }
  *{box-sizing:border-box;margin:0;padding:0}
  html,body{width:1200px;height:800px;overflow:hidden}
  body{background:var(--stage);font-family:"Arimo",Arial,sans-serif;color:var(--ink)}

  .brochure{position:absolute;left:60px;top:60px;width:1080px;height:680px;background:var(--paper);overflow:hidden}
  .panel{position:absolute;top:0;width:360px;height:680px}
  .panel-trust{left:0}
  .panel-back{left:360px}
  .panel-cover{left:720px}

  /* ribbon flag */
  .flag{position:absolute;width:96px;text-align:center;color:var(--white);font-size:12px;line-height:1.3}
  .flag svg{position:absolute;inset:0;width:100%;height:100%}
  .flag span{position:relative;display:block;padding-top:14px}

  .photo{position:absolute}

  /* field photo area across inner panels */
  .field{position:absolute;left:360px;top:200px;width:720px;height:300px;background:linear-gradient(180deg,var(--green-field),var(--green-field-deep))}
  .green-wave{position:absolute;left:360px;top:420px;width:720px;height:260px}

  /* left panel */
  .photo-produce{left:0;top:0;width:360px;height:190px;background:linear-gradient(135deg,#a8733d,#8a5a3a)}
  .panel-trust .flag{left:28px;top:78px;height:96px}
  .trust-title{position:absolute;left:34px;top:206px;color:var(--orange);font-weight:700;font-size:19px}
  .trust-text{position:absolute;left:34px;top:234px;width:296px;font-size:13.5px;line-height:1.35}
  .steps{position:absolute;left:24px;top:312px;width:312px;list-style:none}
  .steps li{display:flex;align-items:center;gap:8px;height:24px;margin-bottom:4px;padding-left:12px;color:var(--white);font-weight:700;font-size:15px}
  .steps .step-call{background:var(--blue)}
  .steps .step-pay{background:var(--green)}
  .steps .step-receive{background:var(--orange)}
  .steps svg{width:14px;height:14px;flex:none}
  .producer-text{position:absolute;left:34px;top:408px;width:296px;font-size:13.5px;line-height:1.35}
  .photo-cattle{left:24px;top:466px;width:150px;height:104px;background:linear-gradient(180deg,#9dbfd8,#7a6a48)}
  .photo-farmer{left:180px;top:462px;width:156px;height:108px;background:linear-gradient(180deg,#4d7a2e,#33521f)}
  .care-band{position:absolute;left:0;bottom:0;width:360px;height:110px;background:var(--green);color:var(--white);text-align:center;padding-top:34px}
  .care-band p{font-size:16px}
  .care-band .phone{display:block;margin-top:2px;font-family:"Archivo Black",sans-serif;font-size:17px;color:var(--ink)}

  /* middle panel */
  .panel-back .flag{left:34px;top:18px;height:80px}
  .offer{position:absolute;left:0;top:112px;width:360px;text-align:center}
  .offer h3{color:var(--red);font-family:"Archivo Black",sans-serif;font-size:15px;letter-spacing:.5px;margin-bottom:2px}
  .offer p{font-size:12px;font-weight:700;letter-spacing:.4px;text-transform:uppercase;line-height:1.3}
  .values{position:absolute;left:0;top:268px;width:360px;text-align:center;color:var(--white);font-family:"Archivo Black",sans-serif;font-size:27px;line-height:1.1;letter-spacing:1px}
  .contact{position:absolute;left:0;top:478px;width:360px;text-align:center;color:var(--white)}
  .brand-box{display:flex;align-items:center;justify-content:center;margin:0 auto 10px;background:var(--white);color:var(--ink);width:124px;height:64px;font-size:13px;line-height:1.2}
  .contact .address{font-size:15px}
  .contact .phone{font-family:"Archivo Black",sans-serif;font-size:17px;color:var(--ink)}
  .contact .email{font-weight:700;font-size:12px}

  /* right panel */
  .brand{position:absolute;left:0;top:30px;width:360px;text-align:center}
  .brand .mark{display:block;width:30px;height:30px;margin:0 auto 10px;background:var(--red)}
  .brand .name{font-size:22px;color:var(--ink)}
  .cover-title{position:absolute;left:0;top:440px;width:360px;text-align:center;font-family:"Archivo Black",sans-serif;font-size:23px;line-height:1.1;color:var(--red)}
  .cover-tagline{position:absolute;left:0;top:546px;width:360px;text-align:center;color:var(--white);font-size:15px;line-height:1.35}
</style>
</head>
<body>
<main class="brochure">
  <div class="field" role="img" aria-label="Campo verde de cultivo"></div>
  <svg class="green-wave" viewBox="0 0 720 260" preserveAspectRatio="none" aria-hidden="true">
    <path d="M0 70 Q180 20 360 70 L360 260 L0 260 Z" fill="var(--green)"/>
    <path d="M360 60 Q540 10 720 50 L720 260 L360 260 Z" fill="var(--green)"/>
  </svg>

  <section class="panel panel-trust">
    <div class="photo photo-produce" role="img" aria-label="Legumes e hortaliças frescas sobre mesa de madeira"></div>
    <div class="flag">
      <svg viewBox="0 0 96 96" preserveAspectRatio="none" aria-hidden="true"><path d="M0 0H96V96L48 80L0 96Z" fill="var(--green)"/></svg>
      <span>Frescos<br>de<br>Qualidade</span>
    </div>
    <h2 class="trust-title">Confie em Qualidade</h2>
    <p class="trust-text">A qualidade de todos os frescos distribuídos por nós é verificada para que apenas os produtos aprovados cheguem até si.</p>
    <ul class="steps">
      <li class="step-call"><svg viewBox="0 0 14 14" aria-hidden="true"><path d="M2 7l3 3 7-8" stroke="#9be06a" stroke-width="2.4" fill="none"/></svg>Encomende por telefone</li>
      <li class="step-pay"><svg viewBox="0 0 14 14" aria-hidden="true"><path d="M2 7l3 3 7-8" stroke="var(--orange)" stroke-width="2.4" fill="none"/></svg>Pague no banco</li>
      <li class="step-receive"><svg viewBox="0 0 14 14" aria-hidden="true"><path d="M2 7l3 3 7-8" stroke="var(--blue)" stroke-width="2.4" fill="none"/></svg>Receba os seus frescos</li>
    </ul>
    <p class="producer-text">Se for produtor e deseja comercializar os seus produtos de forma segura, contacte-nos hoje!</p>
    <div class="photo photo-cattle" role="img" aria-label="Gado num pasto"></div>
    <div class="photo photo-farmer" role="img" aria-label="Agricultor a carregar um cesto de fruta"></div>
    <footer class="care-band">
      <p>Manuseamos com cuidado</p>
      <span class="phone">+244 900 123 456</span>
    </footer>
  </section>

  <section class="panel panel-back">
    <div class="flag">
      <svg viewBox="0 0 96 80" preserveAspectRatio="none" aria-hidden="true"><path d="M0 0H96V80L48 66L0 80Z" fill="var(--green)"/></svg>
      <span>Entregamos<br>à sua porta</span>
    </div>
    <div class="offer">
      <h3>FAZEMOS DESCONTOS</h3>
      <p>Fazemos descontos a<br>clientes com contratos de<br>fornecimento contínuo</p>
    </div>
    <h2 class="values">QUALIDADE<br>RAPIDEZ<br>SATISFAÇÃO</h2>
    <div class="contact">
      <div class="brand-box">Every Window<br>Bright</div>
      <p class="address">Bairro Verde, Luanda</p>
      <p class="phone">+244 900 123 456</p>
      <p class="email">contacto@everywindowbright.ao</p>
    </div>
  </section>

  <section class="panel panel-cover">
    <div class="brand">
      <span class="mark"></span>
      <span class="name">Every Window Bright</span>
    </div>
    <h1 class="cover-title">Hortaliças<br>Frutas Carnes<br>Peixes Mariscos</h1>
    <p class="cover-tagline">Levamos produtos frescos<br>Nacionais à sua porta.</p>
  </section>
</main>
</body>
</html>
```